Business Card Design

We would like a colorful, engaging, welcoming business card, utilizing our picture of a local lighthouse. We are a Church. We would like the design to mostly feature the colour blue.
Thank you so much to all Designers who sent in submissions to us - it was really hard to make a decision, they were all of such high quality. We would not hesitate to recommend Sketch Harbor to other churches/ businesses.
Kestrel Beacon Fellowship
Industry/Entity Type
Business
Contact Information for Business Card
Kestrel Beacon Fellowship Inc, 17 Merrow Rd, TALLOWVALE WA 6412, Ph: (08) 9517 4063, E: beaconfellowship@quorvex.example, Facebook logo - Kestrel Beacon Fellowship Inc, Sunday Service 10am, "For God sent not his Son into the world to condemn the world; but that the world through Him might be saved." John 3:17.

```html
<!DOCTYPE html>
<html lang="en">
<head>
<meta charset="utf-8">
<title>Kestrel Beacon Fellowship Inc – Business Card</title>
<link rel="stylesheet" href="https://fonts.googleapis.com/css2?family=Jost:wght@800&family=Open+Sans:wght@400&family=Roboto+Condensed:wght@400;500&display=swap">
<style>
  :root {
    --stage: #2a2a2e;
    --night-deep: #0d1e5c;
    --night-mid: #1f3f9a;
    --night-glow: #5d86d6;
    --hill: #3d4a3a;
    --band-navy: #171a5e;
    --band-blue: #2a3f9e;
    --band-sky: #22a6e0;
    --stripe-grey: #c9ccd2;
    --stripe-blue: #3aa8e4;
    --white: #ffffff;
    --ink: #111111;
  }
  * { margin: 0; padding: 0; box-sizing: border-box; }
  html, body {
    width: 1200px; height: 999px; overflow: hidden;
    background: var(--stage);
  }
  .card {
    position: absolute; left: 80px; top: 202px;
    width: 1040px; height: 595px; overflow: hidden;
    background: var(--night-deep);
  }
  .scene-photo {
    position: absolute; inset: 0 0 120px 0;
    background:
      radial-gradient(ellipse 260px 200px at 330px 150px, rgba(190,215,255,.75), transparent 70%),
      linear-gradient(to bottom, transparent 62%, var(--hill) 88%),
      linear-gradient(160deg, var(--night-deep) 0%, var(--night-mid) 45%, var(--night-glow) 75%, var(--night-mid) 100%);
  }
  .band { position: absolute; left: 0; top: 0; width: 1040px; height: 595px; }
  .verse {
    position: absolute; left: 630px; top: 62px; width: 370px;
    font-family: "Open Sans", sans-serif; font-size: 23px; line-height: 1.3;
    color: var(--white);
  }
  .verse-ref { margin-top: 22px; font-size: 22px; }
  .service-time {
    position: absolute; left: 640px; top: 318px;
    background: var(--white); color: var(--ink);
    font-family: "Open Sans", sans-serif; font-size: 22px;
    padding: 4px 16px; border-radius: 18px;
  }
  .org-name {
    position: absolute; left: 36px; top: 478px;
    font-family: "Jost", sans-serif; font-weight: 800; font-size: 35px;
    color: var(--white); letter-spacing: .5px;
  }
  .contact-row {
    position: absolute; left: 36px; top: 536px; right: 20px;
    display: flex; align-items: center; gap: 12px;
    font-family: "Roboto Condensed", sans-serif; color: var(--white);
  }
  .divider { width: 2px; height: 40px; background: var(--white); }
  .contact-address { font-size: 16px; margin-right: 14px; }
  .contact-phone { font-size: 25px; font-weight: 500; margin-right: 14px; }
  .contact-email { font-size: 17px; }
  .icon { flex: none; }
</style>
</head>
<body>
  <article class="card">
    <div class="scene-photo" role="img" aria-label="Night photograph of a lighthouse on a grassy hill with beams of light radiating across a deep blue sky"></div>

    <svg class="band" viewBox="0 0 1040 595" aria-hidden="true">
      <defs>
        <linearGradient id="band-fill" x1="0" y1="0" x2="1" y2="0">
          <stop offset="0" stop-color="var(--band-navy)"/>
          <stop offset=".55" stop-color="var(--band-blue)"/>
          <stop offset="1" stop-color="var(--band-sky)"/>
        </linearGradient>
      </defs>
      <path d="M0 448 Q520 362 1040 432 L1040 595 L0 595 Z" fill="var(--stripe-grey)"/>
      <path d="M0 462 Q520 378 1040 448 L1040 595 L0 595 Z" fill="var(--stripe-blue)"/>
      <path d="M0 472 Q520 390 1040 460 L1040 595 L0 595 Z" fill="url(#band-fill)"/>
    </svg>

    <blockquote class="verse">
      <p>"for God sent not his Son into the world to condemn the world; but that the world through him might be saved"</p>
      <p class="verse-ref">John 3:17</p>
    </blockquote>

    <div class="service-time">Sunday Service 10am</div>

    <h1 class="org-name">Kestrel Beacon Fellowship Inc,</h1>

    <div class="contact-row">
      <svg class="icon" width="36" height="36" viewBox="0 0 36 36" aria-hidden="true" fill="none" stroke="#fff" stroke-width="2">
        <circle cx="18" cy="18" r="16"/>
        <ellipse cx="18" cy="18" rx="7" ry="16"/>
        <line x1="2" y1="18" x2="34" y2="18"/>
        <path d="M5 10 H31 M5 26 H31"/>
      </svg>
      <span class="divider"></span>
      <span class="contact-address">17 Merrow Rd, TALLOWVALE WA 6412,</span>
      <svg class="icon" width="34" height="34" viewBox="0 0 34 34" aria-hidden="true">
        <rect width="34" height="34" rx="4" fill="#fff"/>
        <path d="M11 7 L15 11 L12.5 14 Q15 20 20 22.5 L23 20 L27 24 L24 27.5 Q13 27 7 12 Z" fill="var(--band-navy)"/>
      </svg>
      <span class="divider"></span>
      <span class="contact-phone">(08) 9517 4063</span>
      <svg class="icon" width="38" height="30" viewBox="0 0 38 30" aria-hidden="true">
        <path d="M2 12 L19 1 L36 12 L36 29 L2 29 Z" fill="#fff"/>
        <path d="M2 12 L19 22 L36 12" fill="none" stroke="var(--band-blue)" stroke-width="2"/>
      </svg>
      <span class="divider"></span>
      <span class="contact-email">beaconfellowship@quorvex.example</span>
    </div>
  </article>
</body>
</html>
```